Business card design for Automotive workshop

We need a business card for a new automotive repair and tyre shop called Ridgeback Prime Automotive located in New Zealand. We are a clean, modern and fresh workshop and company.

Front needs to feature logo,
my name:
Lachie Westergaard (director)

Address:
48 Marlow Lane
Ngaroa Bay 3574

Phone: 07 842 1937
Mobile: 027 519 2764
Email: office@ridgebackmotors.co.nz
Website: ridgebackmotors.co.nz

Back needs to feature an area to write down appointment details, date and time.

Also feature a list of jobs and work we do such as,
Vehicle Servicing
All Mechanical Repairs
Warrant of Fitness
Tyres & Wheel Alignments
Automotive Diagnostics
Automotive Parts & Supplies

```html
<!DOCTYPE html>
<html lang="en">
<head>
<meta charset="utf-8">
<title>Ridgeback Prime Automotive – Business Card</title>
<link href="https://fonts.googleapis.com/css2?family=Lato:wght@400;700&display=swap" rel="stylesheet">
<style>
  :root {
    --stage: #e0e0e0;
    --card-dark: #000000;
    --card-light: #ffffff;
    --brand-red: #e3202a;
    --ink: #111111;
    --ink-inverse: #ffffff;
    --muted: #8e8e8e;
    --rule-dark: #9a9a9a;
    --rule-light: #8a8a8a;
  }
  * { box-sizing: border-box; margin: 0; padding: 0; }
  html, body {
    width: 1200px; height: 960px; overflow: hidden;
    background: var(--stage);
    font-family: "Lato", "Helvetica Neue", Arial, sans-serif;
  }
  .canvas { position: relative; width: 1200px; height: 960px; }

  .card {
    position: absolute; left: 280px; width: 655px; height: 374px;
    border-radius: 26px; overflow: hidden;
  }
  .card--front { top: 80px; background: var(--card-dark); color: var(--ink-inverse); }
  .card--back { top: 506px; background: var(--card-light); color: var(--ink); }

  .brand-name {
    position: absolute; color: var(--brand-red);
    font-weight: 700; text-transform: uppercase; letter-spacing: 1px; line-height: 1.05;
  }
  .card--front .brand-name { right: 55px; top: 58px; text-align: right; font-size: 27px; }
  .card--back .brand-name { left: 58px; top: 52px; font-size: 28px; }

  .person { position: absolute; left: 52px; top: 144px; }
  .person__name { color: var(--brand-red); font-size: 25px; font-weight: 700; line-height: 1.2; }
  .person__role { font-size: 18.5px; line-height: 1.3; }

  .divider {
    position: absolute; left: 52px; top: 214px; width: 548px; height: 1px;
    background: var(--rule-dark);
  }

  .contacts { position: absolute; left: 52px; top: 234px; list-style: none; }
  .contacts li {
    display: flex; align-items: center; gap: 8px;
    font-size: 17.5px; height: 23.7px;
  }
  .contacts svg { width: 13px; height: 13px; flex: none; }

  .address {
    position: absolute; right: 55px; top: 277px; text-align: right;
    font-size: 18px; line-height: 24px; font-style: normal;
  }

  .appointment__title {
    position: absolute; left: 63px; top: 136px; font-size: 25px; font-weight: 700;
  }
  .field {
    position: absolute; font-size: 17.5px; color: var(--muted);
  }
  .field-line { position: absolute; height: 1px; background: var(--rule-light); }

  .services { position: absolute; left: 63px; top: 261px; list-style: none; width: 570px; }
  .services li {
    display: inline-flex; align-items: center; gap: 9px;
    font-size: 17.5px; color: var(--muted); height: 23.5px; margin-right: 7px;
  }
  .services li::before {
    content: ""; width: 10px; height: 10px;
    border: 2px solid var(--brand-red); flex: none;
  }
</style>
</head>
<body>
<div class="canvas">

  <section class="card card--front" aria-label="Card front">
    <div class="brand-name">Ridgeback Prime<br>Automotive</div>

    <div class="person">
      <p class="person__name">Lachie Westergaard</p>
      <p class="person__role">Director</p>
    </div>

    <div class="divider"></div>

    <ul class="contacts">
      <li>
        <svg viewBox="0 0 16 16" aria-hidden="true"><path d="M3 1.5 6 4.5 4.5 6.5c1 2 3 4 5 5L11.5 10l3 3-2 2C6.5 14.5 1.5 9.5 1 3.5z" fill="var(--brand-red)"/></svg>
        07 842 1937
      </li>
      <li>
        <svg viewBox="0 0 16 16" aria-hidden="true"><rect x="4" y="1" width="8" height="14" rx="1.5" fill="none" stroke="var(--brand-red)" stroke-width="1.6"/><circle cx="8" cy="12.5" r="0.9" fill="var(--brand-red)"/></svg>
        027 519 2764
      </li>
      <li>
        <svg viewBox="0 0 16 16" aria-hidden="true"><rect x="1" y="3.5" width="14" height="9" fill="var(--brand-red)"/><path d="M1 3.5 8 9l7-5.5" fill="none" stroke="var(--card-dark)" stroke-width="1.2"/></svg>
        office@ridgebackmotors.co.nz
      </li>
      <li>
        <svg viewBox="0 0 16 16" aria-hidden="true"><g fill="none" stroke="var(--brand-red)" stroke-width="1.2"><circle cx="8" cy="8" r="6.5"/><ellipse cx="8" cy="8" rx="3" ry="6.5"/><path d="M1.5 8h13M2.6 4.5h10.8M2.6 11.5h10.8"/></g></svg>
        www.ridgebackmotors.co.nz
      </li>
    </ul>

    <address class="address">48 Marlow Lane,<br>Ngaroa Bay 3574</address>
  </section>

  <section class="card card--back" aria-label="Card back">
    <div class="brand-name">Ridgeback Prime<br>Automotive</div>

    <h2 class="appointment__title">Appointment</h2>

    <span class="field" style="left:62px; top:181px;">Name :</span>
    <span class="field-line" style="left:126px; top:198px; width:463px;"></span>

    <span class="field" style="left:62px; top:218px;">Date&nbsp;&nbsp;&nbsp;:</span>
    <span class="field-line" style="left:126px; top:235px; width:180px;"></span>
    <span class="field" style="left:313px; top:218px;">Time&nbsp;&nbsp;:</span>
    <span class="field-line" style="left:375px; top:235px; width:211px;"></span>

    <ul class="services">
      <li>Vehicle Servicing</li>
      <li>All Mechanical Repairs</li>
      <li>Warrant of Fitness</li>
      <li>Tyres &amp; Wheel Alignments</li>
      <li>Automotive Diagnostics</li>
      <li>Automotive Parts &amp; Supplies</li>
    </ul>
  </section>

</div>
</body>
</html>
```